Company or website name
- Plate Rover Restaurant Delivery Service LLC
- Links to the website
- We are a restaurant marketing and delivery company. We market restaurants and deliver their food.
- Other Facts

```html
<!DOCTYPE html>
<html lang="en">
<head>
<meta charset="utf-8">
<title>Plate Rover Restaurant Delivery Service LLC — Menu</title>
<link rel="stylesheet" href="https://fonts.googleapis.com/css2?family=Kaushan+Script&family=Lora:wght@400&display=swap">
<style>
  :root {
    --sheet: #000000;
    --ink: #f4efe8;
    --heading-red: #c4161c;
    --brand-orange: #ef9a48;
    --card-light: #ffffff;
    --card-blush: #efdcd6;
    --warm-1: #7a4a22;
    --warm-2: #4a2a14;
    --warm-3: #2a170b;
    --photo-warm: #c98447;
    --photo-light: #e6c7a4;
  }
  * { box-sizing: border-box; margin: 0; padding: 0; }
  html, body {
    width: 1200px; height: 960px; overflow: hidden;
    background: var(--sheet);
  }
  .menu {
    position: relative; width: 1200px; height: 960px;
    background: var(--sheet);
    font-family: "Lora", serif;
    color: var(--ink);
  }
  .menu__ambience {
    position: absolute; left: 0; top: 0; width: 1200px; height: 520px;
    background: linear-gradient(180deg, var(--warm-1) 0%, var(--warm-2) 25%, var(--warm-3) 50%, var(--sheet) 100%);
  }
  .section-title {
    position: absolute;
    font-family: "Kaushan Script", cursive;
    font-weight: 400;
    font-size: 68px;
    line-height: 1;
    color: var(--heading-red);
    white-space: nowrap;
  }
  .section-title--appetizers { left: 33px; top: 28px; }
  .section-title--dessert { left: 633px; top: 28px; }
  .section-title--main { left: 30px; top: 694px; letter-spacing: 5px; }
  .dish-list {
    position: absolute; list-style: none; width: 545px;
  }
  .dish-list--appetizers { left: 30px; top: 131px; }
  .dish-list--dessert { left: 630px; top: 131px; }
  .dish-list--main { left: 30px; top: 792px; }
  .dish-list--extra { left: 630px; top: 702px; }
  .dish {
    display: flex; align-items: baseline;
    height: 32px;
    font-size: 22px; letter-spacing: 5px;
  }
  .dish__leader {
    flex: 1; height: 4px; margin: 0 8px 0 2px;
    background-image: radial-gradient(circle, var(--ink) 1.3px, transparent 1.6px);
    background-size: 10px 4px;
    background-repeat: repeat-x;
  }
  .dish__price { letter-spacing: 0; }
  .panel {
    position: absolute; top: 377px; width: 512px; height: 308px;
    border-radius: 11px; overflow: hidden;
  }
  .panel--photo {
    left: 43px;
    background: linear-gradient(135deg, var(--photo-warm) 0%, var(--photo-light) 100%);
  }
  .panel--brand {
    left: 643px;
    display: flex; flex-direction: column; align-items: center; justify-content: center;
    gap: 18px; text-align: center; padding: 0 36px;
    background: linear-gradient(180deg, var(--card-light) 0%, var(--card-blush) 100%);
    color: var(--brand-orange);
    font-family: "Lora", serif;
    font-weight: 400;
  }
  .brand-name { font-size: 32px; line-height: 1.3; }
  .brand-link { font-size: 20px; color: var(--brand-orange); text-decoration: none; letter-spacing: 1px; }
</style>
</head>
<body>
  <main class="menu">
    <div class="menu__ambience" role="img" aria-label="Blurred warm restaurant interior fading into black"></div>

    <h2 class="section-title section-title--appetizers">Appetizers</h2>
    <ul class="dish-list dish-list--appetizers">
      <li class="dish"><span class="dish__name">Menu1</span><span class="dish__leader"></span><span class="dish__price">3</span></li>
      <li class="dish"><span class="dish__name">Menu2</span><span class="dish__leader"></span><span class="dish__price">3</span></li>
      <li class="dish"><span class="dish__name">Menu3</span><span class="dish__leader"></span><span class="dish__price">3</span></li>
      <li class="dish"><span class="dish__name">Menu4</span><span class="dish__leader"></span><span class="dish__price">3</span></li>
      <li class="dish"><span class="dish__name">Menu5</span><span class="dish__leader"></span><span class="dish__price">3</span></li>
      <li class="dish"><span class="dish__name">Menu6</span><span class="dish__leader"></span><span class="dish__price">3</span></li>
      <li class="dish"><span class="dish__name">Menu7</span><span class="dish__leader"></span><span class="dish__price">3</span></li>
    </ul>

    <h2 class="section-title section-title--dessert">Dessert</h2>
    <ul class="dish-list dish-list--dessert">
      <li class="dish"><span class="dish__name">Menu1</span><span class="dish__leader"></span><span class="dish__price">3</span></li>
      <li class="dish"><span class="dish__name">Menu2</span><span class="dish__leader"></span><span class="dish__price">3</span></li>
      <li class="dish"><span class="dish__name">Menu3</span><span class="dish__leader"></span><span class="dish__price">3</span></li>
      <li class="dish"><span class="dish__name">Menu4</span><span class="dish__leader"></span><span class="dish__price">3</span></li>
      <li class="dish"><span class="dish__name">Menu5</span><span class="dish__leader"></span><span class="dish__price">3</span></li>
      <li class="dish"><span class="dish__name">Menu6</span><span class="dish__leader"></span><span class="dish__price">3</span></li>
      <li class="dish"><span class="dish__name">Menu7</span><span class="dish__leader"></span><span class="dish__price">3</span></li>
    </ul>

    <div class="panel panel--photo" role="img" aria-label="Photo of a plated restaurant dish"></div>

    <div class="panel panel--brand">
      <span class="brand-name">Plate Rover Restaurant Delivery Service LLC</span>
      <a class="brand-link" href="https://www.platerover.example">www.platerover.example</a>
    </div>

    <h2 class="section-title section-title--main">Main Dish</h2>
    <ul class="dish-list dish-list--main">
      <li class="dish"><span class="dish__name">Menu1</span><span class="dish__leader"></span><span class="dish__price">3</span></li>
      <li class="dish"><span class="dish__name">Menu2</span><span class="dish__leader"></span><span class="dish__price">3</span></li>
      <li class="dish"><span class="dish__name">Menu3</span><span class="dish__leader"></span><span class="dish__price">3</span></li>
      <li class="dish"><span class="dish__name">Menu4</span><span class="dish__leader"></span><span class="dish__price">3</span></li>
    </ul>

    <ul class="dish-list dish-list--extra">
      <li class="dish"><span class="dish__name">Menu1</span><span class="dish__leader"></span><span class="dish__price">3</span></li>
      <li class="dish"><span class="dish__name">Menu2</span><span class="dish__leader"></span><span class="dish__price">3</span></li>
      <li class="dish"><span class="dish__name">Menu3</span><span class="dish__leader"></span><span class="dish__price">3</span></li>
      <li class="dish"><span class="dish__name">Menu4</span><span class="dish__leader"></span><span class="dish__price">3</span></li>
      <li class="dish"><span class="dish__name">Menu5</span><span class="dish__leader"></span><span class="dish__price">3</span></li>
      <li class="dish"><span class="dish__name">Menu6</span><span class="dish__leader"></span><span class="dish__price">3</span></li>
      <li class="dish"><span class="dish__name">Menu7</span><span class="dish__leader"></span><span class="dish__price">3</span></li>
    </ul>
  </main>
</body>
</html>
```